Visitenkarten-Design für Sonnen-/Fensterschutz
Zielgruppe
KLR GmbH ist eine Firma, die Sonnenschutz und Fensterschutz anbieten.
'Ihr kompetenter Partner in Sachen Sonnenschutz- , Fenster- und Türtechnik. Sie erhalten echtes Handwerk aus dem Mühlviertel zu fairen Preisen.'
Unsere Zielgruppe sind Personen mit Haus, die am Land leben.
Firmenname: KLR GmbH
Slogan: Fenster & Sonnenschutz
Aufgabenstellung
Hier befindet sich das Logodesign: https://dl.qv/t-Rm8pQ2wZtB
Bitte ein schlichtes Design bereitstellen mit einer Dummy-Person:
Lutz Brenneke + Telefonnummer + Email
Die finalen Daten bitte erst am Schluss berücksichtigen (für Gewinnerdesign)
Gerne auch hintern + vorne bedruckbar bereitstellen.

```html
<!DOCTYPE html>
<html lang="de">
<head>
<meta charset="utf-8">
<title>KLR GmbH – Visitenkarte</title>
<link href="https://fonts.googleapis.com/css2?family=Open+Sans:wght@400;600&family=Poppins:wght@400;600;700&display=swap" rel="stylesheet">
<style>
  :root {
    --stage: #585858;
    --paper: #ffffff;
    --ink: #4a4a4a;
    --rule: #d6d6d6;
    --orange: #ee7a22;
    --red: #e03a22;
    --deep-red: #9c1e1a;
  }
  * { box-sizing: border-box; margin: 0; padding: 0; }
  html, body { width: 1200px; height: 1200px; overflow: hidden; }
  body { background: var(--stage); position: relative; font-family: "Poppins", sans-serif; color: var(--ink); }

  .card { position: absolute; left: 278px; width: 633px; height: 410px; background: var(--paper); overflow: hidden; }
  .card--front { top: 138px; }
  .card--back { top: 666px; }

  .divider { position: absolute; left: 265px; top: 33px; width: 1px; height: 282px; background: var(--rule); }

  .person { position: absolute; left: 0; width: 265px; top: 102px; text-align: center; font-family: "Open Sans", sans-serif; }
  .person__name { font-size: 21px; font-weight: 400; color: var(--ink); }
  .person__role { font-size: 15px; font-weight: 600; color: var(--ink); margin-top: 2px; }

  .contact { position: absolute; left: 38px; top: 203px; font-size: 16px; line-height: 1.05; }
  .contact__company { font-size: 15px; font-weight: 600; color: #8a8a8a; margin-bottom: 8px; }
  .contact__row { display: flex; align-items: flex-start; gap: 6px; margin-bottom: 12px; }
  .contact__row svg { flex: none; width: 18px; height: 18px; margin-top: 1px; }

  .brand { position: absolute; left: 285px; top: 130px; width: 348px; text-align: center; }
  .brand__name { font-weight: 700; font-size: 46px; color: var(--orange); line-height: 1; }
  .brand__slogan { font-weight: 600; font-size: 15px; color: var(--deep-red); letter-spacing: 0.5px; margin-top: 6px; border-top: 2px solid var(--deep-red); display: inline-block; padding-top: 3px; }

  .stripes { position: absolute; left: 0; top: 347px; width: 633px; height: 50px; }
  .stripe { position: absolute; left: 0; width: 100%; background: linear-gradient(90deg, var(--red), var(--orange) 60%, var(--red)); }
  .stripe--a { top: 4px; height: 3px; }
  .stripe--b { top: 12px; height: 12px; }
  .stripe--c { top: 28px; height: 3px; }
  .stripe--d { top: 34px; height: 12px; }
  .stripe-mark { position: absolute; left: 463px; top: 0; width: 64px; height: 50px; background: var(--paper); display: flex; align-items: center; justify-content: center; font-weight: 700; font-size: 17px; color: var(--red); }

  .back-brand { position: absolute; inset: 0; display: flex; align-items: center; justify-content: center; font-weight: 700; font-size: 110px; color: var(--orange); }
</style>
</head>
<body>
  <section class="card card--front">
    <div class="person">
      <p class="person__name">Lutz Brenneke</p>
      <p class="person__role">Geschäftsführer</p>
    </div>

    <div class="contact">
      <p class="contact__company">KLR GmbH</p>
      <div class="contact__row">
        <svg viewBox="0 0 18 18" aria-hidden="true"><path d="M1 3 L17 9 L1 15 L5 9 Z" fill="var(--red)"/></svg>
        <span>Am Lindenhang 7<br>4240 Freistadt</span>
      </div>
      <div class="contact__row">
        <svg viewBox="0 0 18 18" aria-hidden="true"><path d="M4 1 L7 1 L8 5 L6 7 Q8 11 11 12 L13 10 L17 11 L17 14 Q15 17 12 16 Q4 13 2 5 Q2 2 4 1 Z" fill="var(--red)"/></svg>
        <span>+49 170 555 0182</span>
      </div>
      <div class="contact__row">
        <svg viewBox="0 0 18 18" aria-hidden="true"><rect x="1" y="4" width="16" height="11" rx="1" fill="var(--red)"/><path d="M1 5 L9 11 L17 5" stroke="#fff" stroke-width="1.5" fill="none"/></svg>
        <span>+49 170 555 0182</span>
      </div>
    </div>

    <div class="divider"></div>

    <div class="brand">
      <p class="brand__name">KLR GmbH</p>
      <p class="brand__slogan">FENSTER &amp; SONNENSCHUTZ</p>
    </div>

    <div class="stripes">
      <div class="stripe stripe--a"></div>
      <div class="stripe stripe--b"></div>
      <div class="stripe stripe--c"></div>
      <div class="stripe stripe--d"></div>
      <div class="stripe-mark">KLR</div>
    </div>
  </section>

  <section class="card card--back">
    <p class="back-brand">KLR GmbH</p>
  </section>
</body>
</html>
```